Electrical company needs professional eye catching business cards

I am an electrician who needs business cards. I have attached two images which you can use. The file ab.jpg I would atleast like to be used. The file named back.jpg can be used on the back or not... up to you.

The information on my business cards I will have displayed will be-
My name
Mobile number
web site url
Licence number
ABN

Also as another request, I would like the word "Electrician" on the front of the card somewhere. Maybe under my name or something?

Industry/Entity Type

Electrician

```html
<!DOCTYPE html>
<html lang="en">
<head>
<meta charset="utf-8">
<title>Kova Installations – Business Card Back</title>
<link rel="stylesheet" href="https://fonts.googleapis.com/css2?family=Lexend:wght@500&display=swap">
<style>
  :root {
    --navy-deep: #0d1430;
    --navy: #1a2a6e;
    --royal: #233f96;
    --indigo: #2b2f7e;
    --silver: #eef0f6;
  }
  * { margin: 0; padding: 0; box-sizing: border-box; }
  html, body {
    width: 1200px;
    height: 685px;
    overflow: hidden;
    background: var(--navy-deep);
  }
  .card-back {
    position: relative;
    width: 1200px;
    height: 685px;
    overflow: hidden;
    background:
      radial-gradient(ellipse 70% 80% at 55% 45%, var(--royal) 0%, rgba(35,63,150,0) 70%),
      linear-gradient(100deg, var(--navy-deep) 0%, var(--navy) 28%, var(--royal) 55%, var(--indigo) 85%, #1b1f55 100%);
  }
  .card-back::after {
    content: "";
    position: absolute;
    inset: 0;
    background:
      repeating-linear-gradient(0deg, rgba(255,255,255,0.025) 0 1px, rgba(0,0,0,0) 1px 4px),
      linear-gradient(90deg, rgba(5,8,20,0.55) 0%, rgba(5,8,20,0) 30%, rgba(5,8,20,0) 80%, rgba(5,8,20,0.35) 100%);
    pointer-events: none;
  }
  .brand {
    position: absolute;
    top: 50%;
    left: 50%;
    transform: translate(-50%, -50%);
    display: flex;
    align-items: center;
    gap: 26px;
    z-index: 1;
  }
  .brand-square {
    width: 118px;
    height: 118px;
    background: var(--silver);
    border-radius: 10px;
    flex: none;
  }
  .brand-name {
    font-family: "Lexend", sans-serif;
    font-weight: 500;
    font-size: 92px;
    line-height: 1;
    letter-spacing: -1px;
    color: var(--silver);
    white-space: nowrap;
  }
</style>
</head>
<body>
  <main class="card-back">
    <div class="brand">
      <span class="brand-square" aria-hidden="true"></span>
      <span class="brand-name">Kova Installations</span>
    </div>
  </main>
</body>
</html>
```